Lanternfield Dance Business Card

I'm looking for a two-sided business card design to promote my country dance busness. Cowboy hats, boots, and wood grain floor textures, are all appropriate to use.
On one side I want it to say:
Lanternfield Dance
with
Mark
Take The Challenge - Experience The Growth
210-574-2318
On the other side I want:
A place for a Head Shot
The Quote: Experience Is The Best Teacher
A two column bullet list with the following:
First column: Two Step, Waltz, Triple Two, Polka
Second column: Cha-Cha, West Coast, East Cost, NightClub
My Name: Mark Delby
My Phone Number: 210-574-2318
Please see attached drawing

```html
<!DOCTYPE html>
<html lang="en">
<head>
<meta charset="utf-8">
<title>Lanternfield Dance – Business Card</title>
<link rel="stylesheet" href="https://fonts.googleapis.com/css2?family=Graduate&family=Alfa+Slab+One&family=Amarante&family=Cabin:wght@700&family=Open+Sans:wght@600&family=Kalam:wght@700&display=swap">
<style>
  :root {
    --page-bg: #e9e4dc;
    --wood-dark: #4a2a17;
    --wood-mid: #6e4327;
    --wood-light: #8a5a37;
    --plank-line: rgba(30, 14, 6, 0.45);
    --gold-light: #ffe1a8;
    --gold: #f3be6c;
    --gold-deep: #d99a48;
    --cream: #fff6ea;
    --shadow: rgba(0, 0, 0, 0.55);
  }
  * { box-sizing: border-box; margin: 0; padding: 0; }
  html, body { width: 900px; height: 1200px; overflow: hidden; }
  body { background: var(--page-bg); position: relative; }

  .card {
    position: absolute;
    left: 95px;
    width: 710px;
    height: 415px;
    border-radius: 18px;
    overflow: hidden;
    background: linear-gradient(100deg, var(--wood-mid) 0%, var(--wood-light) 35%, var(--wood-mid) 65%, var(--wood-dark) 100%);
    box-shadow: 0 6px 16px rgba(0, 0, 0, 0.35);
  }
  .card--front { top: 130px; }
  .card--back  { top: 600px; }

  .planks { position: absolute; inset: 0; }

  .abs { position: absolute; }
  .centered { transform: translateX(-50%); text-align: center; white-space: nowrap; }

  /* front */
  .dancers-art {
    left: 365px; top: 35px;
    width: 340px; height: 350px;
    border-radius: 12px;
    background: linear-gradient(160deg, var(--gold) 0%, var(--gold-light) 55%, var(--gold-deep) 100%);
    opacity: 0.85;
  }
  .brand-name {
    left: 197px; top: 86px;
    font: 34px "Graduate", serif;
    color: var(--cream);
    text-shadow: 2px 3px 3px var(--shadow);
    transform: translateX(-50%) scaleX(0.74);
    z-index: 1;
  }
  .brand-with {
    left: 197px; top: 130px;
    font: 17px "Alfa Slab One", serif;
    color: var(--gold);
    letter-spacing: 1px;
    text-shadow: 1px 2px 2px var(--shadow);
  }
  .brand-host {
    left: 197px; top: 148px;
    font: 50px "Alfa Slab One", serif;
    color: var(--gold);
    background: linear-gradient(var(--gold-light), var(--gold-deep));
    -webkit-background-clip: text;
    background-clip: text;
    -webkit-text-fill-color: transparent;
    filter: drop-shadow(2px 3px 2px var(--shadow));
  }
  .tagline {
    left: 197px; top: 222px;
    font: 23px/27px "Amarante", serif;
    color: var(--cream);
    text-shadow: 1px 2px 2px var(--shadow);
  }
  .phone-front {
    left: 197px; top: 296px;
    font: 700 38px "Cabin", sans-serif;
    color: var(--gold);
    letter-spacing: 1px;
    text-shadow: 2px 3px 3px var(--shadow);
  }

  /* back */
  .headshot {
    left: 50px; top: 47px;
    width: 240px; height: 286px;
    border-radius: 22px;
    background: radial-gradient(ellipse at 50% 40%, #6e4a36 0%, #4b2f22 70%, #3a241a 100%);
    box-shadow: 0 4px 10px var(--shadow);
  }
  .person-name {
    left: 170px; top: 343px;
    font: 700 34px "Cabin", sans-serif;
    color: var(--gold);
    text-shadow: 1px 2px 2px var(--shadow);
  }
  .quote {
    left: 502px; top: 46px;
    font: 32px/46px "Graduate", serif;
    font-weight: 400;
    color: var(--cream);
    text-shadow: 2px 3px 3px var(--shadow);
  }
  .quote-accent { color: var(--gold); }

  .styles-list {
    left: 345px; top: 155px;
    width: 330px;
    list-style: none;
    display: grid;
    grid-template-columns: 170px 160px;
    grid-auto-flow: column;
    grid-template-rows: repeat(4, 39px);
  }
  .styles-list li {
    font: 600 21px "Open Sans", sans-serif;
    color: var(--cream);
    text-shadow: 1px 2px 2px var(--shadow);
    display: flex; align-items: center; gap: 10px;
  }
  .styles-list li::before {
    content: "";
    width: 13px; height: 13px;
    border-radius: 50%;
    background: var(--gold);
    flex: none;
  }
  .phone-back {
    left: 502px; top: 325px;
    font: 700 46px "Kalam", cursive;
    font-style: italic;
    color: var(--cream);
    letter-spacing: 2px;
    text-shadow: 2px 3px 3px var(--shadow);
  }
</style>
</head>
<body>

<section class="card card--front">
  <svg class="planks" width="710" height="415" aria-hidden="true">
    <g stroke="var(--plank-line)" stroke-width="2">
      <line x1="0" y1="70" x2="710" y2="70"/>
      <line x1="0" y1="150" x2="710" y2="150"/>
      <line x1="0" y1="225" x2="710" y2="225"/>
      <line x1="0" y1="300" x2="710" y2="300"/>
      <line x1="0" y1="365" x2="710" y2="365"/>
    </g>
  </svg>
  <div class="abs dancers-art" role="img" aria-label="Gold silhouettes of a cowgirl and cowboy line dancing in hats and boots"></div>
  <div class="abs centered brand-name">LANTERNFIELD DANCE</div>
  <div class="abs centered brand-with">WITH</div>
  <div class="abs centered brand-host">MARK</div>
  <div class="abs centered tagline">Take The Challenge<br>Experience The Growth</div>
  <div class="abs centered phone-front">210-574-2318</div>
</section>

<section class="card card--back">
  <svg class="planks" width="710" height="415" aria-hidden="true">
    <g stroke="var(--plank-line)" stroke-width="2">
      <line x1="0" y1="60" x2="710" y2="60"/>
      <line x1="0" y1="140" x2="710" y2="140"/>
      <line x1="0" y1="220" x2="710" y2="220"/>
      <line x1="0" y1="300" x2="710" y2="300"/>
      <line x1="0" y1="370" x2="710" y2="370"/>
    </g>
  </svg>
  <div class="abs headshot" role="img" aria-label="Head shot of dance instructor Mark Delby"></div>
  <div class="abs centered person-name">Mark Delby</div>
  <h2 class="abs centered quote">EXPERIENCE IS THE<br><span class="quote-accent">BEST TEACHER</span></h2>
  <ul class="abs styles-list">
    <li>Waltz</li>
    <li>Triple Two</li>
    <li>Two Step</li>
    <li>Polka</li>
    <li>Cha-Cha</li>
    <li>West Coast</li>
    <li>East Cost</li>
    <li>NightClub</li>
  </ul>
  <div class="abs centered phone-back">210-574-2318</div>
</section>

</body>
</html>
```